DVD / USB CASE COVER For Educational Software

We are an educational software company
Until today we supplied our software to clients on 5 DVDs
We are now going to combine all the 5 DVDs into a single USB flash drive - The flash drive will be packaged in a Case similar to A DVD case (see image "case sample")
We looking for a new updated design for the USB case to combine and replace all our 5 DVDs (see attached current DVDs artwork)
The new design does not need to be similar to the old ones but it should be related to the topics of our programs :
Maths
English
Afrikaans
Study methods
Accounting (grade 12 only)
Science (Grade 12 only)
Please see attached our logo as well
Please go into our website to the video section http://www.brightquillo.co.za/videos/
to get a feeling of what our software is about
The design should be single sided.
Case size 189 X 273MM

Target Market(s)

Parents to vhilden in school

Industry/Entity Type

Software

Colors

Designer to choose colors to be used in the design.

Requirements
Must have
• Details of the topics of our programs :
• Maths
• English
• Afrikaans
• Study methods
• Accounting (grade 12 only)
• Science (Grade 12 only)
• Case size 189 X 273MM
Nice to have
• A new fresh new look to give parents the feeling of a high qualty software that will help their children in school
Should not have
• please donst use the color yellow

```html
<!DOCTYPE html>
<html lang="en">
<head>
<meta charset="utf-8">
<title>BrightQuill Learning – Case Cover</title>
<link href="https://fonts.googleapis.com/css2?family=Poppins:ital,wght@0,800;1,800&family=Baloo+2:wght@700;800&family=Arimo:ital,wght@0,400;0,700;1,400&display=swap" rel="stylesheet">
<style>
  :root {
    --page-bg: #e6e6e6;
    --cover-bg: #fbfbfb;
    --frame-line: #a9d6e2;
    --title-ink: #353535;
    --accent-blue: #1b86a9;
    --band-blue: #1983a6;
    --deep-teal: #27525d;
    --card-white: #f7f7f7;
    --badge-gold: #c9a227;
    --badge-gold-dark: #9c7a12;
    --text-white: #ffffff;
  }
  * { box-sizing: border-box; margin: 0; padding: 0; }
  html, body { width: 1200px; height: 1200px; overflow: hidden; }
  body {
    background: var(--page-bg);
    display: flex; align-items: center; justify-content: center;
  }
  .cover {
    position: relative;
    width: 760px; height: 1098px; /* 189 x 273 mm ratio */
    background: var(--cover-bg);
    box-shadow: 0 18px 40px rgba(0,0,0,.18);
    overflow: hidden;
  }
  .cover-frame {
    position: absolute; inset: 24px;
    border: 1.5px solid var(--frame-line);
  }
  .photo-strip { position: absolute; left: 64px; top: 86px; width: 632px; height: 250px; }
  .brush-wash {
    position: absolute; left: 70px; top: 400px; width: 630px; height: 300px;
    border-radius: 45% 40% 50% 35%;
    background:
      radial-gradient(ellipse at 20% 40%, rgba(244,170,190,.45), transparent 55%),
      radial-gradient(ellipse at 45% 30%, rgba(190,230,170,.45), transparent 55%),
      radial-gradient(ellipse at 75% 45%, rgba(160,205,240,.5), transparent 60%),
      radial-gradient(ellipse at 55% 75%, rgba(240,160,170,.3), transparent 55%);
    filter: blur(6px);
  }
  .title {
    position: absolute; left: 96px; top: 470px;
    font-family: "Poppins", sans-serif; font-weight: 800; font-style: italic;
    font-size: 74px; line-height: 1.0; letter-spacing: 1px;
    color: var(--title-ink); text-transform: uppercase;
    white-space: nowrap;
  }
  .title-rule {
    position: absolute; left: 96px; top: 622px; width: 170px; height: 3px;
    background: var(--title-ink);
  }
  .subtitle {
    position: absolute; left: 96px; top: 628px;
    font-family: "Arimo", sans-serif; font-size: 30px; color: var(--accent-blue);
  }
  .topics-heading {
    position: absolute; left: 300px; top: 760px;
    font-family: "Baloo 2", sans-serif; font-weight: 800; font-style: italic;
    font-size: 27px; color: var(--accent-blue); text-transform: uppercase;
    text-decoration: underline; text-decoration-thickness: 2px; text-underline-offset: 3px;
  }
  .info-band {
    position: absolute; left: 64px; top: 850px; width: 632px; height: 185px;
    background: var(--band-blue); border-radius: 0 0 28px 28px;
  }
  .topics-card {
    position: absolute; left: 150px; top: 800px; width: 540px; height: 150px;
    background: var(--card-white); border-radius: 0 0 26px 26px;
    box-shadow: 0 8px 14px rgba(0,0,0,.25);
  }
  .topic-list {
    position: absolute; left: 120px; top: 10px; width: 170px;
    list-style: none; text-align: center;
    font-family: "Baloo 2", sans-serif; font-weight: 700; font-style: italic;
    font-size: 21px; line-height: 1.15; color: #111;
  }
  .senior-topics {
    position: absolute; left: 300px; top: 12px; width: 210px; height: 96px;
    background: var(--deep-teal); border-radius: 12px;
    box-shadow: 0 5px 10px rgba(0,0,0,.3);
    color: var(--text-white); text-align: center;
    font-family: "Baloo 2", sans-serif; font-weight: 700; font-style: italic;
    font-size: 19px; line-height: 1.15; padding-top: 8px;
  }
  .senior-topics .senior-label {
    display: inline-block; border-bottom: 1px solid rgba(255,255,255,.6); padding-bottom: 1px;
  }
  .approval-seal { position: absolute; left: 78px; top: 790px; width: 170px; height: 170px; }
  .band-note {
    position: absolute; left: 110px; top: 975px; width: 300px;
    font-family: "Arimo", sans-serif; font-style: italic; font-size: 14px;
    line-height: 1.25; color: var(--text-white);
  }
  .band-divider {
    position: absolute; left: 440px; top: 962px; width: 1.5px; height: 58px;
    background: rgba(255,255,255,.8);
  }
  .grade-range {
    position: absolute; left: 462px; top: 966px;
    font-family: "Arimo", sans-serif; font-style: italic; font-weight: 700;
    font-size: 19px; line-height: 1.2; color: var(--text-white);
  }
  .grade-range span { font-weight: 400; font-size: 17px; }
</style>
</head>
<body>
  <main class="cover">
    <div class="cover-frame"></div>

    <svg class="photo-strip" viewBox="0 0 632 250" role="img" aria-label="Photo strip: a smiling girl wearing headphones, a boy writing in class, and students listening to a teacher in a classroom">
      <defs>
        <linearGradient id="photoOne" x1="0" y1="0" x2="1" y2="1">
          <stop offset="0" stop-color="#c9a98a"/><stop offset="1" stop-color="#5b3b30"/>
        </linearGradient>
        <linearGradient id="photoTwo" x1="0" y1="0" x2="1" y2="1">
          <stop offset="0" stop-color="#e7dfd8"/><stop offset="1" stop-color="#8a3a36"/>
        </linearGradient>
        <linearGradient id="photoThree" x1="0" y1="0" x2="1" y2="1">
          <stop offset="0" stop-color="#8e9aa8"/><stop offset="1" stop-color="#4a3a3a"/>
        </linearGradient>
      </defs>
      <path d="M0 26 Q0 0 26 0 H196 V160 Q196 186 170 186 H150 Q130 186 130 206 V250 H0 Z" fill="url(#photoOne)"/>
      <rect x="200" y="0" width="204" height="146" fill="url(#photoTwo)"/>
      <path d="M408 0 H606 Q632 0 632 26 V120 Q632 146 606 146 H408 Z" fill="url(#photoThree)"/>
    </svg>

    <div class="brush-wash" role="img" aria-label="Soft pastel watercolour brush strokes"></div>

    <h1 class="title">BrightQuill<br>Learning</h1>
    <div class="title-rule"></div>
    <p class="subtitle">Educational Software</p>

    <div class="info-band"></div>
    <h2 class="topics-heading">Consists of 6 topics!!</h2>

    <section class="topics-card">
      <ul class="topic-list">
        <li>Study Methods</li>
        <li>Maths</li>
        <li>English</li>
        <li>Afrikaans</li>
      </ul>
      <div class="senior-topics">
        <span class="senior-label">Grade 12 Only!</span><br>
        Accounting<br>
        Science
      </div>
    </section>

    <svg class="approval-seal" viewBox="0 0 170 170" role="img" aria-label="Approval seal">
      <circle cx="85" cy="85" r="82" fill="var(--badge-gold-dark)"/>
      <circle cx="85" cy="85" r="74" fill="var(--badge-gold)"/>
      <circle cx="85" cy="85" r="60" fill="none" stroke="var(--badge-gold-dark)" stroke-width="3"/>
    </svg>

    <p class="band-note">This program specifically based on the school curriculum to help our kids exceed!!</p>
    <div class="band-divider"></div>
    <p class="grade-range">GRADES <span>?-?</span><br>AGES <span>?-?</span></p>
  </main>
</body>
</html>
```